Need Edgy Web Design Home Page for Entertainment Agency

We need a web design splash page for our entertainment company, Vexa Prime Agency based (Los Angeles and New York).
Vexa Prime is a full service PR, marketing and special events agency based in Los Angeles and New York. We aim to serve the most elite in entertainment, media and sports.

With a combined experience of over 30 years in the entertainment industry, our team is committed to deliver each client with the upmost service and contemporary strategies to increase your business objective.

CREATIVE, EDGY & TRENDSETTING

SERVICES

PR Campaigns

Media Relations

Talent Representation

Brand Marketing & Activations

Special Events: Publicity & Consulting

EXPERTISE

Television

Film

Talent

Music

Marketing & Promotions

Industry Events

Digital & Social Media

Looking for a home page that is flashy, edgy and creative. I've provided our logos and contact details:

Delia Fortunez
dfortunez@kelvoritla.com

Tobias Renn
trenn@kelvoritny.com

Paloma Quiroga
pquiroga@kelvoritla.com

Target Market(s)

Los Angeles and New York

Industry/Entity Type

Entertainment

Number of Pages Required

1 page

Font styles to use
Serif
Decorative

Requirements
Must have
• 1. Logo
• 2. Description of services but done creatively
• 4. Visuals (Stock images: cool edgy millennials & graphics images that make sense for our agency)
• 5. Contact Details
• Reference: https://www.tunelathery.net & http://www.thevolrenagency.com
Nice to have
• If possible would love to have stock cartoon images included as images of Delia and I. Reference image (http://www.pixmerrow.com/pic-482915306/stock-vector-cute-cartoon-characters-young-boy-and-girl-in-cool-casual-outfits.html)
Should not have
• Should not look boring!

```html
<!DOCTYPE html>
<html lang="en">
<head>
<meta charset="utf-8">
<title>Vexa Prime Agency</title>
<link href="https://fonts.googleapis.com/css2?family=Roboto+Condensed:wght@300;400;700&family=Open+Sans:ital,wght@0,400;0,600;1,400&display=swap" rel="stylesheet">
<style>
:root{
  --ink:#2f2e33;
  --ink-deep:#262529;
  --sun:#fed55a;
  --sun-deep:#f7c83f;
  --paper:#ffffff;
  --mist:#f3f4f6;
  --text-dark:#333238;
  --muted:#6c6b70;
  --line:#55545a;
}
*{box-sizing:border-box;margin:0;padding:0}
html,body{width:1200px;height:2410px;overflow:hidden}
body{position:relative;background:var(--sun);font-family:"Open Sans",Arial,sans-serif;color:var(--text-dark)}
.abs{position:absolute}
.cond{font-family:"Roboto Condensed","Arial Narrow",sans-serif}

/* header + hero */
.hero{left:0;top:0;width:1200px;height:660px;background:var(--ink)}
.logo{display:flex;align-items:center;gap:12px;color:var(--sun);font-family:"Roboto Condensed","Arial Narrow",sans-serif;font-weight:400;font-size:34px;letter-spacing:1px;line-height:1}
.logo .dot{width:46px;height:46px;border-radius:50%;background:var(--sun)}
.nav{top:54px;left:427px;display:flex;align-items:center;font-family:"Roboto Condensed","Arial Narrow",sans-serif;font-size:15px;color:var(--paper);text-transform:uppercase}
.nav a{color:inherit;text-decoration:none;position:absolute;white-space:nowrap}
.nav .current::after{content:"";position:absolute;left:0;right:0;top:30px;height:2px;background:var(--sun)}
.signup{position:absolute;left:1020px;top:47px;width:81px;height:30px;background:var(--sun);color:var(--ink);border-radius:3px;font-family:"Roboto Condensed","Arial Narrow",sans-serif;font-size:13px;display:flex;align-items:center;justify-content:center}
.hero-title{left:98px;top:268px;font-size:62px;font-weight:700;color:var(--paper);letter-spacing:1px;line-height:1}
.hero-copy{left:98px;top:346px;width:340px;font-size:12.5px;line-height:21px;color:var(--paper)}
.dots{left:98px;top:441px;display:flex;gap:6px}
.dots span{width:14px;height:14px;border-radius:50%;border:1.5px solid #ddd}
.dots span.on{background:#e8eef6}
.crew{left:440px;top:135px;width:640px;height:500px;border-radius:40px;background:radial-gradient(ellipse at 50% 55%,#4f6a7a 0%,#3c4148 55%,rgba(47,46,51,0) 78%)}

/* services */
.section-title{width:1200px;left:0;text-align:center;font-family:"Roboto Condensed","Arial Narrow",sans-serif;color:var(--text-dark)}
.services-title{top:694px;font-size:31px}
.service{width:240px;text-align:center}
.service .badge{width:116px;height:116px;margin:0 auto;border-radius:50%;background:var(--ink);border:3px solid var(--paper);box-shadow:0 14px 14px -8px rgba(0,0,0,.18);display:flex;align-items:center;justify-content:center}
.service .label{margin-top:30px;font-size:16px;color:var(--text-dark);text-transform:uppercase;font-family:"Open Sans",Arial,sans-serif}

/* welcome */
.welcome-title{top:1060px;font-size:40px;font-weight:300;color:var(--paper)}
.welcome-title .hi{color:var(--sun)}
.welcome-copy{left:180px;top:1124px;width:840px;text-align:center;font-size:12.5px;line-height:21px;color:var(--paper)}
.more{left:538px;top:1205px;width:124px;height:38px;border:1.5px solid #d8d8d8;border-radius:3px;color:var(--paper);font-size:13px;display:flex;align-items:center;justify-content:center;gap:6px}

/* agency */
.video{left:100px;top:1351px;width:450px;height:269px;background:linear-gradient(180deg,#34496d 0%,#b0523a 48%,#f0a12f 62%,#1f1e22 78%)}
.video .bar{position:absolute;left:12px;right:12px;bottom:10px;height:22px;background:rgba(20,20,24,.8);border-radius:2px}
.video .track{position:absolute;left:10px;top:9px;width:310px;height:4px;background:#555}
.video .track i{display:block;width:150px;height:4px;background:#3aa0d8}
.play{position:absolute;left:198px;top:114px;width:54px;height:34px;background:rgba(255,255,255,.85);border-radius:4px}
.play::after{content:"";position:absolute;left:22px;top:10px;border-left:12px solid #444;border-top:7px solid transparent;border-bottom:7px solid transparent}
.agency-title{left:582px;top:1362px;font-size:27px;color:var(--text-dark)}
.agency-copy{left:584px;top:1405px;width:520px;font-size:11px;line-height:18px}
.ticks{left:586px;top:1481px;list-style:none;font-size:12.5px}
.ticks li{height:34.5px;display:flex;align-items:flex-start;gap:12px}
.ticks svg{margin-top:4px}

/* testimonials */
.quotes{left:0;top:1680px;width:1200px;height:380px;background:linear-gradient(100deg,#fbfcfd 0%,#f1f3f6 55%,#e2e5ea 80%,#f2f3f5 100%)}
.quotes-title{top:1740px;font-size:33px;font-weight:300;color:#3d3c42}
.quote{width:400px;border-left:1px solid #ccc;padding-left:26px}
.quote p{font-style:italic;font-size:13px;line-height:23px;color:#3d3c42;position:relative}
.quote p::before{content:"\201C";position:absolute;left:-12px;top:-8px;font-size:24px;color:#888}
.author{display:flex;align-items:center;gap:22px;margin-top:22px;margin-left:-10px}
.avatar{width:76px;height:76px;border-radius:50%;border:3px solid var(--paper);box-shadow:0 2px 6px rgba(0,0,0,.2)}
.author .who{font-style:italic;font-size:12.5px;line-height:21px;color:#6c6b70}
.serrate{left:0;top:2044px;width:1200px;height:12px;background:linear-gradient(135deg,var(--mist) 50%,transparent 50%) 0 0/12px 12px repeat-x,linear-gradient(225deg,var(--mist) 50%,transparent 50%) 0 0/12px 12px repeat-x}

/* footer */
.footer{left:0;top:2050px;width:1200px;height:360px;background:var(--ink)}
.foot-logo{left:100px;top:2120px}
.social{left:128px;top:2188px;display:flex;gap:6px}
.social span{width:26px;height:26px;border-radius:3px;background:#d6d6d8}
.foot-head{font-family:"Roboto Condensed","Arial Narrow",sans-serif;font-size:15.5px;color:var(--paper);text-transform:uppercase}
.contact-line{display:flex;gap:14px;color:var(--paper);font-size:12px;line-height:20px}
.form-copy{left:633px;top:2128px;width:470px;font-size:11px;line-height:18px;color:var(--paper)}
.field{height:40px;border:1px solid #4a494f;color:#8b8a90;font-size:11px;padding:0 14px;display:flex;align-items:center}
.send{left:874px;top:2232px;width:227px;height:40px;background:var(--sun);color:var(--ink);font-size:14px;display:flex;align-items:center;justify-content:center;text-transform:uppercase}
.copyright{left:0;width:1200px;top:2350px;text-align:center;font-size:12px;color:var(--text-dark)}
.foot-links{left:0;width:1200px;top:2376px;text-align:center;font-size:12px;color:var(--text-dark)}
</style>
</head>
<body>

<div class="abs hero"></div>
<div class="abs crew" role="img" aria-label="Cartoon illustration of five young team members with a phone, laptop and speech bubble"></div>

<svg class="abs" style="left:0;top:505px" width="1200" height="170" viewBox="0 0 1200 170" aria-hidden="true">
  <g fill="var(--sun)">
    <rect x="0" y="100" width="1200" height="70"/>
    <circle cx="-10" cy="90" r="50"/><circle cx="60" cy="100" r="40"/><circle cx="125" cy="112" r="32"/>
    <circle cx="190" cy="112" r="34"/><circle cx="255" cy="118" r="30"/><circle cx="320" cy="122" r="32"/>
    <circle cx="390" cy="124" r="30"/><circle cx="460" cy="120" r="34"/><circle cx="530" cy="116" r="36"/>
    <circle cx="600" cy="118" r="34"/><circle cx="665" cy="120" r="32"/><circle cx="730" cy="115" r="36"/>
    <circle cx="800" cy="106" r="42"/><circle cx="870" cy="92" r="46"/><circle cx="940" cy="80" r="50"/>
    <circle cx="1010" cy="68" r="50"/><circle cx="1075" cy="60" r="50"/><circle cx="1140" cy="45" r="50"/>
    <circle cx="1200" cy="40" r="50"/>
  </g>
</svg>

<div class="abs logo" style="left:100px;top:42px">VEXA PRIME<span class="dot"></span></div>
<nav class="abs nav">
  <a class="current" style="left:0;top:0">Home</a>
  <a style="left:78px;top:0">About Vexa Prime</a>
  <a style="left:245px;top:0">Our Services</a>
  <a style="left:380px;top:0">Expertise</a>
  <a style="left:484px;top:0">Contact Us</a>
</nav>
<div class="signup">SIGN UP</div>

<h1 class="abs hero-title cond">VEXA PRIME</h1>
<p class="abs hero-copy">Vexa Prime is a full service PR, marketing and special events agency based in Los Angeles and New York. We aim to serve the most elite in entertainment, media and sports.</p>
<div class="abs dots"><span class="on"></span><span></span><span></span></div>

<h2 class="abs section-title services-title">OUR SERVICES</h2>

<div class="abs service" style="left:84px;top:765px">
  <div class="badge"><svg width="44" height="44" viewBox="0 0 24 24" fill="var(--sun)"><path d="M3 10h3l9-5v14l-9-5H3z"/><path d="M6 14l2 6h3l-2-6z"/><rect x="17" y="10" width="3" height="4" rx="1"/></svg></div>
  <div class="label">PR Campaigns</div>
</div>
<div class="abs service" style="left:351px;top:765px">
  <div class="badge"><svg width="44" height="44" viewBox="0 0 24 24" fill="none" stroke="var(--sun)" stroke-width="2"><rect x="9" y="3" width="6" height="11" rx="3" fill="var(--sun)"/><path d="M6 11a6 6 0 0 0 12 0M12 17v4M9 21h6"/></svg></div>
  <div class="label">Media Relations</div>
</div>
<div class="abs service" style="left:616px;top:765px">
  <div class="badge"><svg width="40" height="44" viewBox="0 0 20 24"><path d="M2 1h11l5 5v17H2z" fill="var(--sun)"/><path d="M5 11h10M5 14h10M5 17h10" stroke="var(--ink)" stroke-width="1.5"/></svg></div>
  <div class="label">Talent Representation</div>
</div>
<div class="abs service" style="left:876px;top:765px">
  <div class="badge"><svg width="46" height="40" viewBox="0 0 24 20" fill="var(--sun)"><rect x="2" y="10" width="3" height="7"/><rect x="7" y="6" width="3" height="11"/><rect x="12" y="9" width="3" height="8"/><rect x="17" y="4" width="3" height="13"/><rect x="0" y="18" width="24" height="1.5"/></svg></div>
  <div class="label">Brand Marketing</div>
</div>

<svg class="abs" style="left:0;top:950px" width="1200" height="360" viewBox="0 0 1200 360" role="img" aria-label="Darkened photo of a runner at the starting line on an outdoor track">
  <defs>
    <linearGradient id="welcomeShade" x1="0" y1="0" x2="1" y2="0">
      <stop offset="0" stop-color="#3a3a3c"/><stop offset=".55" stop-color="#48484a"/><stop offset="1" stop-color="#3d4238"/>
    </linearGradient>
  </defs>
  <path d="M0 20 L210 8 L625 62 L1110 8 L1200 26 L1200 330 L1010 300 L610 345 L160 300 L0 335 Z" fill="url(#welcomeShade)"/>
</svg>
<h2 class="abs section-title welcome-title">WELCOME TO <span class="hi">VEXA PRIME</span></h2>
<p class="abs welcome-copy">Vexa Prime is a full service PR, marketing and special events agency based in Los Angeles. We aim to serve the most elite in entertainment, media and sports. With a combined experience of over 30 years in the entertainment industry, our team is committed to deliver each client with the upmost service and contemporary strategies to increase your business objective.</p>
<div class="abs more">READ MORE <svg width="13" height="13" viewBox="0 0 12 12"><circle cx="6" cy="6" r="6" fill="#fff"/><path d="M5 3.5 7.5 6 5 8.5" stroke="var(--ink)" stroke-width="1.6" fill="none"/></svg></div>

<div class="abs video" role="img" aria-label="Video still of a city skyline silhouette at sunset">
  <div class="play"></div>
  <div class="bar"><div class="track"><i></i></div></div>
</div>
<h2 class="abs agency-title cond">PR, MARKETING &amp; SPECIAL EVENTS AGENCY</h2>
<p class="abs agency-copy">Lorem ipsum dolor sit amet, consectetur adipisicing elit, sed do eiusmod tempor incididunt ut labore et dolore magna aliqua. Ut enim ad minim veniam, quis nostrud exercitation ullamco laboris Lorem ipsum dolor sit amet, consectetur adipisicing elit.</p>
<ul class="abs ticks">
  <li><svg width="12" height="10" viewBox="0 0 12 10"><path d="M1 5l3.5 3.5L11 1" stroke="var(--text-dark)" stroke-width="2" fill="none"/></svg>Nemo enim ipsam voluptatem quia</li>
  <li><svg width="12" height="10" viewBox="0 0 12 10"><path d="M1 5l3.5 3.5L11 1" stroke="var(--text-dark)" stroke-width="2" fill="none"/></svg>Sed ut perspiciatis unde omnis iste natus</li>
  <li><svg width="12" height="10" viewBox="0 0 12 10"><path d="M1 5l3.5 3.5L11 1" stroke="var(--text-dark)" stroke-width="2" fill="none"/></svg>Lorem ipsum dolor sit amet, consectetur</li>
  <li><svg width="12" height="10" viewBox="0 0 12 10"><path d="M1 5l3.5 3.5L11 1" stroke="var(--text-dark)" stroke-width="2" fill="none"/></svg>Duis aute irure dolor in reprehenderit</li>
</ul>

<div class="abs quotes" role="img" aria-label="Faded photo of a smiling man using a phone"></div>
<svg class="abs" style="left:0;top:1670px" width="1200" height="30" viewBox="0 0 1200 30" aria-hidden="true">
  <path d="M0 16 Q150 4 300 14 T600 10 T900 14 T1200 8 L1200 30 L0 30Z" fill="#fbfcfd"/>
</svg>
<h2 class="abs section-title quotes-title">WHAT OTHERS SAY ABOUT US</h2>
<div class="abs quote" style="left:131px;top:1830px">
  <p>Lorem ipsum dolor sit amet, consectetur adipisicing elit, sed do eiusmod tempor incididunt ut labore et dolore magna aliqua Unde omnis, consequuntur.</p>
  <div class="author"><div class="avatar" style="background:linear-gradient(160deg,#c9a27a,#e8d2bf)" role="img" aria-label="Portrait photo of client"></div><div class="who">JOHN DOE<br>Fernleaf Goods,</div></div>
</div>
<div class="abs quote" style="left:655px;top:1830px">
  <p>Lorem ipsum dolor sit amet, consectetur adipisicing elit, sed do eiusmod tempor incididunt ut labore et dolore magna aliqua Unde omnis, consequuntur.</p>
  <div class="author"><div class="avatar" style="background:linear-gradient(160deg,#4a3a30,#9a7a64)" role="img" aria-label="Portrait photo of client"></div><div class="who">JOHN DOE<br>Fernleaf Goods,</div></div>
</div>

<div class="abs footer"></div>
<div class="abs serrate"></div>

<div class="abs logo foot-logo">VEXA PRIME<span class="dot"></span></div>
<div class="abs social"><span></span><span></span><span></span></div>

<h3 class="abs foot-head" style="left:320px;top:2098px">Contacts</h3>
<div class="abs contact-line" style="left:320px;top:2137px"><svg width="14" height="18" viewBox="0 0 14 18"><path d="M7 0a6 6 0 0 0-6 6c0 4.5 6 12 6 12s6-7.5 6-12a6 6 0 0 0-6-6z" fill="#fff"/><circle cx="7" cy="6" r="2.3" fill="var(--ink)"/></svg><span>Vexa Prime<br>PO Box 4418, Marlow Bay NSW 2190</span></div>
<div class="abs contact-line" style="left:320px;top:2193px;font-size:13.5px"><svg width="16" height="16" viewBox="0 0 24 24"><path d="M6.6 10.8a15 15 0 0 0 6.6 6.6l2.2-2.2c.3-.3.7-.4 1-.2 1.1.4 2.3.6 3.6.6.6 0 1 .4 1 1V20c0 .6-.4 1-1 1A17 17 0 0 1 3 4c0-.6.4-1 1-1h3.5c.6 0 1 .4 1 1 0 1.3.2 2.5.6 3.6.1.3 0 .7-.2 1z" fill="#fff"/></svg><span>Call Us: 1 555 204 7731</span></div>
<div class="abs contact-line" style="left:320px;top:2224px"><svg width="14" height="14" viewBox="0 0 14 12" style="margin-top:3px"><rect x="0" y="1" width="14" height="10" fill="#fff"/><path d="M0 1l7 5 7-5" stroke="var(--ink)" stroke-width="1.3" fill="none"/></svg><span>info@kelvoritla.com</span></div>

<h3 class="abs foot-head" style="left:633px;top:2098px">Contact Form</h3>
<p class="abs form-copy">Lorem ipsum dolor sit amet, consectetur adipiscing elit, sed do eiusmod tempor incididunt ut labore et dolore magna aliqua. Ut enim ad minim veniam,</p>
<div class="abs field" style="left:633px;top:2181px;width:227px">Name</div>
<div class="abs field" style="left:874px;top:2181px;width:227px">E - Mail</div>
<div class="abs field" style="left:633px;top:2232px;width:227px">Phone No</div>
<div class="abs send">Signup Now</div>

<svg class="abs" style="left:0;top:2300px" width="1200" height="110" viewBox="0 0 1200 110" aria-hidden="true">
  <path d="M0 22 Q200 4 400 18 T800 16 T1200 10 L1200 110 L0 110Z" fill="var(--sun)"/>
</svg>
<p class="abs copyright">© 2015 Vexa Prime All rights reserved.</p>
<p class="abs foot-links">Home | &nbsp; About Us &nbsp;| &nbsp; Services &nbsp;| &nbsp; 24/7 Telephone | Contact Us</p>

</body>
</html>
```